Business Card Design - Will Pick Design in 24 Hours

I am looking for a simple, luxury, yet eye catching business card for my electronic business. The business is called Velmorix and I have attached the logo to this job.

The business card must have the following details:

1. Name
2. Email Address
3. Website
4. Position

```html
<!DOCTYPE html>
<html lang="en">
<head>
<meta charset="utf-8">
<title>Velmorix Business Card</title>
<link href="https://fonts.googleapis.com/css2?family=Lora:wght@400;700&family=Montserrat:wght@500&display=swap" rel="stylesheet">
<style>
  :root {
    --teal: #2fb89e;
    --teal-light: #3cc7ac;
    --teal-dark: #27a58d;
    --white: #ffffff;
    --ink: #5a5f63;
    --bg: #ecefee;
    --text-soft: #e3f6f1;
  }
  * { margin: 0; padding: 0; box-sizing: border-box; }
  html, body { width: 1200px; height: 900px; overflow: hidden; background: var(--bg); }
  .card {
    position: absolute;
    left: 270px;
    width: 660px;
    height: 377px;
    border-radius: 4px;
    overflow: hidden;
    box-shadow: 0 6px 18px rgba(0,0,0,0.12);
  }
  /* Back of card */
  .card-back {
    top: 50px;
    background: linear-gradient(160deg, var(--teal-dark), var(--teal-light));
  }
  .brand {
    position: absolute;
    top: 60px; left: 0; right: 0;
    text-align: center;
    color: var(--white);
  }
  .brand-dot {
    display: block;
    width: 46px; height: 46px;
    margin: 0 auto 18px;
    border: 3px solid var(--white);
    border-radius: 50%;
  }
  .brand-name {
    font-family: "Montserrat", sans-serif;
    font-weight: 500;
    font-size: 30px;
    letter-spacing: 3px;
  }
  .web-band {
    position: absolute;
    left: 0; right: 0;
    top: 210px; height: 74px;
    background: rgba(255,255,255,0.14);
    display: flex; align-items: center; justify-content: center;
    font-family: "Lora", serif;
    font-size: 22px;
    letter-spacing: 9px;
    color: var(--white);
  }
  /* Front of card */
  .card-front {
    top: 473px;
    background: var(--white);
  }
  .holder {
    position: absolute;
    right: 40px; top: 34px;
    text-align: right;
    font-family: "Lora", serif;
  }
  .holder-name {
    font-size: 46px;
    font-weight: 700;
    line-height: 1;
    color: var(--teal);
  }
  .holder-name .surname { color: var(--ink); font-weight: 400; }
  .holder-position {
    margin-top: 6px;
    font-size: 19px;
    color: var(--teal);
  }
  .contact-band {
    position: absolute;
    left: 0; right: 0;
    top: 128px; height: 196px;
    background: linear-gradient(180deg, var(--teal-light), var(--teal));
    display: flex;
    justify-content: space-around;
    padding: 0 30px;
  }
  .contact {
    width: 180px;
    display: flex; flex-direction: column; align-items: center;
    padding-top: 24px;
    font-family: "Lora", serif;
    font-size: 15px;
    line-height: 1.35;
    color: var(--text-soft);
    text-align: center;
  }
  .contact svg { width: 96px; height: 96px; margin-bottom: 14px; }
</style>
</head>
<body>
  <section class="card card-back">
    <div class="brand">
      <span class="brand-dot"></span>
      <div class="brand-name">VELMORIX</div>
    </div>
    <div class="web-band">www.velmorix.com</div>
  </section>

  <section class="card card-front">
    <div class="holder">
      <div class="holder-name">Your Full <span class="surname">Name</span></div>
      <div class="holder-position">Your Position</div>
    </div>
    <div class="contact-band">
      <div class="contact contact-address">
        <svg viewBox="0 0 96 96" aria-hidden="true">
          <circle cx="48" cy="48" r="45" fill="none" stroke="#fff" stroke-width="2" stroke-dasharray="7 5"/>
          <path d="M48 26a11 11 0 0 1 11 11c0 8-11 19-11 19s-11-11-11-19a11 11 0 0 1 11-11z" fill="none" stroke="#fff" stroke-width="2.5"/>
          <circle cx="48" cy="37" r="4" fill="#fff"/>
          <ellipse cx="48" cy="66" rx="12" ry="4" fill="none" stroke="#fff" stroke-width="2.5"/>
        </svg>
        <span>Your address, 2443/1<br>#street no, Division</span>
      </div>
      <div class="contact contact-phone">
        <svg viewBox="0 0 96 96" aria-hidden="true">
          <circle cx="48" cy="48" r="45" fill="none" stroke="#fff" stroke-width="2" stroke-dasharray="7 5"/>
          <rect x="38" y="28" width="20" height="40" rx="4" fill="none" stroke="#fff" stroke-width="2.5"/>
          <rect x="42" y="34" width="12" height="12" fill="#fff"/>
          <circle cx="48" cy="58" r="3" fill="#fff"/>
        </svg>
        <span>01xxxxxxxxxxx<br>1234568</span>
      </div>
      <div class="contact contact-email">
        <svg viewBox="0 0 96 96" aria-hidden="true">
          <circle cx="48" cy="48" r="45" fill="none" stroke="#fff" stroke-width="2" stroke-dasharray="7 5"/>
          <rect x="30" y="36" width="36" height="24" fill="none" stroke="#fff" stroke-width="2.5"/>
          <path d="M30 36l18 14 18-14" fill="none" stroke="#fff" stroke-width="2.5"/>
        </svg>
        <span>email@velmorix.com</span>
      </div>
    </div>
  </section>
</body>
</html>
```